Flyer-Design für 2-jährige Ausbildung in medizinischer Kosmetik gesucht
Tolle Designvorschläge, die gut die Vorgaben umgesetzt haben. Änderungswünsche und Fertigstellung erfolgten zügig und professionell. Unbedingt empfehlenswert.
Zielgruppe
2-jährige Vollzeitausbildung in Medizinische Kosmetik an einer Berufsfachschule in privater Trägerschaft (Schulgeld erforderlich, Förderung durch Bafög und der QZ möglich). Zielgruppe sind junge Frauen ab 16, die eine Ausbildung suchen.
Aufgabenstellung
Wir wünschen uns ein freches und modernes Design, das die 50-jährige Tradition der Privatschule und die klassische Schulausbildung aber trotzdem berücksichtigt.
Wünschenswert wäre die Einbindung eines zum Slogan passenden Bildes (Zeichnung oder Comics). Überwiegend in den Schulfarben gehalten (weiß, grün, grau/silber). Ein Plakat (DIN A 3) plus dazu passender Postkarte.

```html
<!DOCTYPE html>
<html lang="de">
<head>
<meta charset="utf-8">
<title>Ausbildung Medizinische Kosmetik – Plakat</title>
<link href="https://fonts.googleapis.com/css2?family=Arimo:wght@400;700&family=Grand+Hotel&display=swap" rel="stylesheet">
<style>
  :root {
    --green: #74ab3c;
    --green-light: #d3e3c1;
    --green-pale: #e9f1e0;
    --grey-bg: #e3e4e6;
    --grey-text: #8a8a8a;
    --body-text: #5b4a55;
    --white: #ffffff;
  }
  * { margin: 0; padding: 0; box-sizing: border-box; }
  html, body { width: 872px; height: 1200px; overflow: hidden; background: var(--white); }
  .poster {
    position: relative; width: 872px; height: 1200px; overflow: hidden;
    font-family: "Arimo", Arial, sans-serif; background: var(--white);
  }
  .hero-bg { position: absolute; left: 0; top: 0; width: 872px; height: 700px; }
  .hero-art {
    position: absolute; left: 0; top: 0; width: 470px; height: 470px;
    background: radial-gradient(ellipse at 55% 45%, #8fc15a 0%, #b5d694 40%, #e4eeda 75%, rgba(255,255,255,0) 100%);
  }
  .headline {
    position: absolute; left: 520px; top: 180px;
    font-family: "Grand Hotel", cursive; color: var(--green);
    font-size: 84px; line-height: 104px;
  }
  .headline span { display: block; position: relative; }
  .headline span::before {
    content: ""; position: absolute; left: -2px; top: 14px;
    width: 80px; height: 80px; border-radius: 50%; background: var(--white); z-index: -1;
  }
  .headline { z-index: 2; isolation: isolate; }
  .badge { position: absolute; left: 22px; top: 376px; width: 200px; height: 200px; }
  .badge-text {
    position: absolute; left: 22px; top: 376px; width: 200px; height: 200px;
    color: var(--white); text-align: center;
  }
  .badge-title { position: absolute; top: 86px; width: 100%; font-size: 20px; }
  .badge-sub { position: absolute; top: 116px; width: 100%; font-size: 12px; letter-spacing: 2px; }
  .intro {
    position: absolute; left: 71px; top: 695px; width: 420px;
    font-size: 18px; line-height: 28px; color: var(--body-text);
  }
  .intro strong { color: var(--green); font-weight: 700; }
  .start-label { position: absolute; left: 71px; top: 865px; font-size: 18px; color: var(--body-text); }
  .start-date {
    position: absolute; left: 68px; top: 895px;
    font-family: "Grand Hotel", cursive; font-size: 66px; color: var(--green);
  }
  .dot-column { position: absolute; left: 392px; top: 868px; width: 16px; height: 330px; }
  .contact {
    position: absolute; left: 549px; top: 863px;
    font-size: 15.5px; line-height: 23px; color: var(--grey-text);
  }
  .contact .gap { height: 23px; }
  .school-name {
    position: absolute; left: 451px; top: 1068px; display: flex; align-items: center; gap: 14px;
  }
  .school-mark { width: 74px; height: 74px; border-radius: 50%; background: var(--green); flex: none; }
  .school-name p {
    font-family: "Arimo", Arial, sans-serif; font-weight: 700; color: var(--green);
    font-size: 21px; line-height: 21px; letter-spacing: 0.5px; text-transform: uppercase;
  }
</style>
</head>
<body>
<main class="poster">
  <svg class="hero-bg" viewBox="0 0 872 700" aria-hidden="true">
    <defs>
      <linearGradient id="sky" x1="0" y1="0" x2="1" y2="0.4">
        <stop offset="0" stop-color="#f4f5f5"/>
        <stop offset="0.55" stop-color="#dcdde0"/>
        <stop offset="1" stop-color="#f1f2f3"/>
      </linearGradient>
    </defs>
    <path d="M0 0 H872 V570 C700 540 520 530 360 470 C240 425 120 420 0 430 Z" fill="url(#sky)"/>
    <path d="M200 460 C360 560 600 620 872 575 V615 C640 650 380 620 200 460 Z" fill="var(--green-light)"/>
    <path d="M210 470 C380 600 640 660 872 600" fill="none" stroke="var(--green)" stroke-width="1.5"/>
    <path d="M230 480 C400 620 660 670 872 625" fill="none" stroke="var(--green)" stroke-width="1.2"/>
    <circle cx="466" cy="530" r="10" fill="var(--green)"/>
    <circle cx="646" cy="545" r="15" fill="var(--green)"/>
    <circle cx="695" cy="543" r="19" fill="var(--green)"/>
    <circle cx="752" cy="540" r="24" fill="var(--green)"/>
  </svg>

  <div class="hero-art" role="img" aria-label="Illustration: Frauengesicht mit Haaren aus grünen Blüten, Ranken und Schmetterlingen"></div>

  <h1 class="headline">
    <span>Beauty</span>
    <span>Health</span>
    <span>Wellness</span>
  </h1>

  <svg class="badge" viewBox="0 0 200 200" aria-hidden="true">
    <circle cx="100" cy="100" r="94" fill="var(--green)"/>
    <g fill="var(--green)">
      <circle cx="100" cy="4" r="8"/><circle cx="100" cy="196" r="8"/>
      <circle cx="4" cy="100" r="8"/><circle cx="196" cy="100" r="8"/>
      <circle cx="32" cy="32" r="8"/><circle cx="168" cy="32" r="8"/>
      <circle cx="32" cy="168" r="8"/><circle cx="168" cy="168" r="8"/>
      <circle cx="63" cy="11" r="8"/><circle cx="137" cy="11" r="8"/>
      <circle cx="63" cy="189" r="8"/><circle cx="137" cy="189" r="8"/>
      <circle cx="11" cy="63" r="8"/><circle cx="11" cy="137" r="8"/>
      <circle cx="189" cy="63" r="8"/><circle cx="189" cy="137" r="8"/>
    </g>
    <circle cx="100" cy="100" r="84" fill="none" stroke="var(--white)" stroke-width="3"/>
    <line x1="52" y1="160" x2="148" y2="160" stroke="var(--white)" stroke-width="2"/>
    <path d="M100 152 L108 160 L100 168 L92 160 Z" fill="var(--green)" stroke="var(--white)" stroke-width="2"/>
  </svg>
  <div class="badge-text">
    <p class="badge-title">staatl. Förderung</p>
    <p class="badge-sub">möglich</p>
  </div>

  <p class="intro">Seit 50 Jahren erfolgreich, bieten wir eine zweijährige anspruchsvolle und qualifizierte Ausbildung zur<br><strong>Medizinischen Kosmetikerin</strong> an.</p>

  <p class="start-label">Nächster Ausbildungsbeginn:</p>
  <p class="start-date">1.Oktober</p>

  <svg class="dot-column" viewBox="0 0 16 330" aria-hidden="true">
    <g fill="var(--green)">
      <circle cx="8" cy="8" r="7.5"/><circle cx="8" cy="32.5" r="7.5"/><circle cx="8" cy="57" r="7.5"/>
      <circle cx="8" cy="81.5" r="7.5"/><circle cx="8" cy="106" r="7.5"/><circle cx="8" cy="130.5" r="7.5"/>
      <circle cx="8" cy="155" r="7.5"/><circle cx="8" cy="179.5" r="7.5"/><circle cx="8" cy="204" r="7.5"/>
      <circle cx="8" cy="228.5" r="7.5"/><circle cx="8" cy="253" r="7.5"/><circle cx="8" cy="277.5" r="7.5"/>
      <circle cx="8" cy="302" r="7.5"/><circle cx="8" cy="322" r="7.5"/>
    </g>
  </svg>

  <address class="contact" style="font-style: normal;">
    <p>SFK Lehrinstitut GmbH</p>
    <p>Ahornweg 17, 10999 Berlin</p>
    <p>T: 030/555 01 23</p>
    <p>F: 030/555 01 247</p>
    <div class="gap"></div>
    <p>kontakt@spreeufer-kosmetikschule.de</p>
    <p>spreeufer-kosmetikschule.de</p>
  </address>

  <div class="school-name">
    <span class="school-mark" aria-hidden="true"></span>
    <p>Spreeufer<br>Fachschule<br>für Kosmetik</p>
  </div>
</main>
</body>
</html>
```